Introducing Us/Sales Person - Sales Flyer

We are a business which manufactures and sells Blinds, Awnings, Curtains, Security Doors. We have sales people driving to customers homes all day every day. The sales team have asked for a small flyer they can give to people they see as they travel or drop into the letterbox of next door neighbors.

I would like a design of a flyer that is upmarket and professional.

It should include information about the business, what products we do and our contact information. It should also introduce the consultant and a small bio on them.

The design must compliment our design bible guidelines and other marketing materials that are attached in a PDF to this document. You can access the design bible here - **removed**
The flyers will be purchased through either https://www.quillmark.com.au/marketing-materials/flyers or http://www.redpelicanpress.com.au/quick-flyers-postcards-brochures-printing.htm. You have creative freedom on the shape and design but remember it needs to be professional, not just a cheap looking a4 page. One option would be a door hanger (https://www.quillmark.com/marketing-materials/door-hangers) although don't restrict yourself to this design format.

Example Content - You can use this or modify it - changing its length, tone or anything you like -

Sales Consultant - Rob Kelner

Rob has been involved in the Blind, Awning & Security Industry for over 40 years with extensive knowledge in both modern and traditional methods of covering doors, windows and outdoor areas.

With a keen eye for symmetry and aesthetics, Rob is able to help customers cut through the many options to the product which will work for their needs and look great in their home.

Rob has an interest in renovating homes with some of his past projects featured in magazines showing that under the sometimes rough exterior is a fine attention to detail and the skill to make your home stand out.

Trained in all our product areas and able to work through even the most complex jobs; he is available to come to your home at a convenient time and help you 'live comfortably' with the addition of Wes Carrow products.

Company Info -

Use our website, examples brochures and the letter attached to steal some appropriate content.

Target Market(s)

Customers aged 35-55
Slightly female focussed

Industry/Entity Type

Home Improvement

Font styles to use
Other font styles liked:
• Gotham

Colors

Designer to choose colors to be used in the design.

Requirements
Must have
• Quality Design
• Appropriate with our logo and other marketing design work
• Professional Look
Nice to have
• Couple of layout options? Maybe door hanger or standard flyer?

```html
<!DOCTYPE html>
<html lang="en">
<head>
<meta charset="utf-8">
<title>Wes Carrow – Screen + Shade Solutions</title>
<link rel="stylesheet" href="https://fonts.googleapis.com/css2?family=Montserrat:wght@400;500;700&display=swap">
<style>
  :root {
    --teal: #0b87a8;
    --white: #ffffff;
    --pale-teal: #b9dde8;
    --rule: #bfc4c7;
    --ink: #4a5154;
    --room-light: #eef0f0;
    --room-mid: #d9dcdc;
    --room-dark: #6d7273;
  }
  html, body {
    margin: 0;
    padding: 0;
    overflow: hidden;
    background: var(--white);
  }
  .flyer {
    position: relative;
    width: 1200px;
    height: 1200px;
    background: var(--white);
    font-family: "Montserrat", sans-serif;
    overflow: hidden;
  }
  .intro-line {
    position: absolute;
    left: 45px;
    top: 118px;
    margin: 0;
    font-size: 15px;
    font-weight: 500;
    letter-spacing: 3px;
    color: var(--teal);
  }
  .brand-band {
    position: absolute;
    left: 0;
    top: 180px;
    width: 1200px;
    height: 214px;
    background: var(--teal);
  }
  .brand-name {
    position: absolute;
    left: 44px;
    top: 126px;
    margin: 0;
    font-size: 44px;
    font-weight: 500;
    letter-spacing: 3px;
    color: var(--white);
    line-height: 1;
  }
  .brand-tagline {
    position: absolute;
    left: 45px;
    top: 172px;
    margin: 0;
    font-size: 15px;
    font-weight: 400;
    letter-spacing: 2px;
    color: var(--pale-teal);
    line-height: 1;
  }
  .room-photo {
    position: absolute;
    left: 0;
    top: 394px;
    width: 1200px;
    height: 486px;
    background: linear-gradient(180deg, var(--room-light) 0%, var(--room-light) 45%, var(--room-mid) 75%, var(--room-dark) 100%);
  }
  .service-bar {
    position: absolute;
    left: 0;
    top: 898px;
    width: 1200px;
    height: 84px;
    display: flex;
  }
  .service-badge {
    width: 162px;
    height: 84px;
    background: var(--teal);
    display: flex;
    align-items: center;
    justify-content: center;
  }
  .service-badge-name {
    font-size: 14px;
    font-weight: 500;
    letter-spacing: 1px;
    color: var(--white);
  }
  .service-details {
    flex: 1;
    border-top: 2px solid var(--rule);
    border-bottom: 2px solid var(--rule);
    box-sizing: border-box;
    position: relative;
  }
  .service-list {
    display: flex;
    justify-content: space-between;
    align-items: center;
    margin: 0;
    padding: 0;
    list-style: none;
    position: absolute;
    left: 16px;
    right: 12px;
    top: 20px;
    font-size: 20px;
    font-weight: 400;
    letter-spacing: 0.8px;
    color: var(--teal);
  }
  .service-list strong { font-weight: 700; }
  .service-contact {
    position: absolute;
    right: 12px;
    top: 54px;
    display: flex;
    align-items: center;
    gap: 30px;
    color: var(--teal);
  }
  .service-url {
    font-size: 13px;
    font-weight: 700;
    letter-spacing: 0.8px;
  }
  .service-mark {
    font-size: 13px;
    font-weight: 500;
    letter-spacing: 1px;
  }
  .consultant {
    position: absolute;
    left: 45px;
    right: 45px;
    top: 1006px;
    display: flex;
    gap: 40px;
  }
  .consultant-card {
    width: 300px;
    flex-shrink: 0;
    border-right: 2px solid var(--rule);
    padding-right: 30px;
  }
  .consultant-role {
    margin: 0 0 6px;
    font-size: 12px;
    font-weight: 500;
    letter-spacing: 2px;
    color: var(--ink);
  }
  .consultant-name {
    margin: 0 0 14px;
    font-size: 26px;
    font-weight: 700;
    letter-spacing: 1.5px;
    color: var(--teal);
  }
  .consultant-phone,
  .consultant-email {
    margin: 0 0 6px;
    font-size: 14px;
    font-weight: 500;
    letter-spacing: 0.6px;
    color: var(--ink);
  }
  .consultant-phone strong { color: var(--teal); font-weight: 700; }
  .consultant-bio {
    flex: 1;
    margin: 0;
    font-size: 13.5px;
    line-height: 1.55;
    font-weight: 400;
    color: var(--ink);
  }
  .consultant-bio p { margin: 0 0 8px; }
</style>
</head>
<body>
  <main class="flyer">
    <p class="intro-line">INTRODUCING YOUR LOCAL CONSULTANT</p>

    <header class="brand-band">
      <h1 class="brand-name">WES CARROW</h1>
      <p class="brand-tagline">SCREEN + SHADE SOLUTIONS</p>
    </header>

    <div class="room-photo" role="img" aria-label="Bright bedroom with white roller blinds half drawn over black-framed windows, a timber chair with cushion, a small side table with plants and a bed with grey throw"></div>

    <section class="service-bar">
      <div class="service-badge">
        <span class="service-badge-name">WES CARROW</span>
      </div>
      <div class="service-details">
        <ul class="service-list">
          <li><strong>WE DO</strong> BLINDS</li>
          <li>|</li>
          <li>CURTAINS</li>
          <li>|</li>
          <li>SHUTTERS</li>
          <li>|</li>
          <li>GUARDMESH</li>
          <li>|</li>
          <li>WINDOW FILM</li>
          <li>|</li>
          <li>AWNINGS</li>
        </ul>
        <div class="service-contact">
          <span class="service-url">WESCARROWSA.COM.AU</span>
          <span class="service-mark">WES CARROW</span>
        </div>
      </div>
    </section>

    <section class="consultant">
      <div class="consultant-card">
        <p class="consultant-role">SALES CONSULTANT</p>
        <h2 class="consultant-name">ROB KELNER</h2>
        <p class="consultant-phone"><strong>M</strong>&nbsp; 0400 000 000</p>
        <p class="consultant-email">rob@wescarrowsa.com.au</p>
      </div>
      <div class="consultant-bio">
        <p>Rob has been in the blind, awning and security industry for over 40 years, with deep knowledge of modern and traditional ways to cover doors, windows and outdoor areas.</p>
        <p>With a keen eye for symmetry and style, Rob helps you cut through the options to the product that suits your needs and looks great in your home. He will visit at a time that suits you and help you live comfortably with Wes Carrow.</p>
      </div>
    </section>
  </main>
</body>
</html>
```